Fantastic Flyer Needed for Harbor Physicians

We have just launched our new business, The Harbor Physicians which is a service to people get a second opinion from the UK.

Please see www.theharborphysicians.example and also visit How It Works, Our Services and other pages on the website.

I would like a double sided A5 size flyer to handout. I am open to all ideas but it has to be visually in line with our brand logo and website.

Target Market(s)

Small and medium size companies in Pakistan, Ex pats in the Middle East and middle class individuals in sub continent.

Industry/Entity Type

Business

Font styles to use
Other font styles liked:
• Open Sans and Muse Sans (500)

Requirements
Must have
• What we do and what our company does
• Getting people to our website and booking page
• That we give basic medical health info for free on videos called Clinicasts
• I tend to like some of the newer infographic styles
Nice to have
• How our service works and the the pricing for the appointment.
• See if we can use the beefeater graphic (i.e. the UK soilder)
Should not have
• Pictures of random doctors, ideally no facial pictures. Do not use stock photos.

```html
<!DOCTYPE html>
<html lang="en">
<head>
<meta charset="utf-8">
<title>Harbor Physicians – Flyer</title>
<link rel="stylesheet" href="https://fonts.googleapis.com/css2?family=Oswald:wght@300;400;500&family=Lato:wght@400;700&display=swap">
<style>
  :root {
    --backdrop: #5a1416;
    --orange: #e05f27;
    --figure-cream: #fdf3e4;
    --figure-gold: #f5a623;
    --ink: #333333;
    --olive: #a49d2f;
    --mustard: #c9972a;
    --teal-dark: #2b5b6c;
    --sage: #87aca2;
    --bronze: #8c6a24;
    --banner: #d69631;
    --brand-grey: #4d4d4d;
    --white: #ffffff;
  }
  * { box-sizing: border-box; margin: 0; padding: 0; }
  html, body { width: 1200px; height: 1000px; overflow: hidden; }
  body { background: var(--backdrop); font-family: "Lato", sans-serif; }

  .flyer {
    position: absolute; left: 240px; top: 0;
    width: 720px; height: 1000px; background: var(--white);
  }
  .stat-band {
    position: absolute; left: 0; top: 0; width: 720px; height: 387px;
    background: var(--orange);
  }
  .stat-question {
    position: absolute; top: 13px; width: 100%; text-align: center;
    font-family: "Oswald", sans-serif; font-weight: 400; font-size: 20.5px;
    color: var(--white);
  }
  .people-chart { position: absolute; left: 0; top: 0; }

  .mission {
    position: absolute; top: 398px; width: 100%; text-align: center;
    font-family: "Oswald", sans-serif; font-weight: 400; font-size: 30px; line-height: 40px;
    text-transform: uppercase; color: var(--ink); letter-spacing: 0;
  }
  .mission .olive { color: var(--olive); }
  .mission .mustard { color: var(--mustard); }
  .mission .orange { color: var(--orange); }
  .mission .teal { color: var(--teal-dark); }
  .mission .bronze { color: var(--bronze); }

  .offer {
    position: absolute; top: 567px; width: 343px; height: 206px;
    color: var(--white); padding: 13px 18px 0 18px;
  }
  .offer--time { left: 14px; background: var(--sage); }
  .offer--guidance { left: 363px; background: var(--teal-dark); }
  .offer h2 {
    font-weight: 700; font-size: 22px; text-align: center; margin-bottom: 22px;
  }
  .offer ul { list-style: none; }
  .offer li {
    position: relative; padding-left: 27px; font-size: 15.5px; line-height: 19px;
    margin-bottom: 16px;
  }
  .offer--guidance li { padding-left: 30px; margin-bottom: 14px; }
  .offer li svg { position: absolute; left: 0; top: 3px; }

  .booking {
    position: absolute; left: 14px; top: 790px; width: 692px; height: 120px;
    background: var(--banner); text-align: center;
  }
  .booking-call {
    font-family: "Oswald", sans-serif; font-weight: 400; font-size: 27px;
    text-transform: uppercase; color: var(--white); margin-top: 13px;
  }
  .booking-link {
    font-weight: 700; font-size: 15.5px; color: var(--white); margin-top: 4px;
  }
  .booking-free {
    font-weight: 700; font-size: 16px; color: var(--ink); margin-top: 11px;
  }

  .brand-name {
    position: absolute; top: 924px; width: 100%; text-align: center;
    font-family: "Oswald", sans-serif; font-weight: 300; font-size: 26px; line-height: 29px;
    text-transform: uppercase; color: var(--brand-grey); letter-spacing: 0.5px;
  }
</style>
</head>
<body>
  <main class="flyer">
    <section class="stat-band">
      <p class="stat-question">Do you know that in average there is only one doctor per 1,000 people in Pakistan?</p>
      <svg class="people-chart" width="720" height="387" viewBox="0 0 720 387" aria-label="One doctor figure above rows of people figures">
        <defs>
          <g id="person">
            <circle cx="17.5" cy="7" r="7"/>
            <rect x="7" y="16" width="21" height="28" rx="4"/>
            <rect x="2" y="17" width="4.5" height="25" rx="2.2"/>
            <rect x="28.5" y="17" width="4.5" height="25" rx="2.2"/>
            <rect x="8.5" y="40" width="8" height="31" rx="3"/>
            <rect x="18.5" y="40" width="8" height="31" rx="3"/>
          </g>
          <pattern id="crowd" width="35" height="76" patternUnits="userSpaceOnUse" x="30" y="143">
            <use href="#person" fill="var(--figure-cream)"/>
          </pattern>
        </defs>
        <use href="#person" fill="var(--figure-gold)" transform="translate(343 55) scale(0.98 1.04)"/>
        <rect x="30" y="143" width="665" height="228" fill="url(#crowd)"/>
      </svg>
    </section>

    <h1 class="mission">
      We are <span class="olive">London based</span> family <span class="mustard">physicians</span> who<br>
      <span class="orange">passionately</span> believe that everyone<br>
      in the world should have <span class="teal">access to a doctor</span> who<br>
      they can <span class="bronze">trust</span>
    </h1>

    <section class="offer offer--time">
      <h2>We'll spend time with you...</h2>
      <ul>
        <li><svg width="14" height="12" viewBox="0 0 14 12"><path d="M1 6.5 5 10.5 13 1.5" fill="none" stroke="#fff" stroke-width="2.6"/></svg>to discuss your history</li>
        <li><svg width="14" height="12" viewBox="0 0 14 12"><path d="M1 6.5 5 10.5 13 1.5" fill="none" stroke="#fff" stroke-width="2.6"/></svg>review your case documents</li>
        <li><svg width="14" height="12" viewBox="0 0 14 12"><path d="M1 6.5 5 10.5 13 1.5" fill="none" stroke="#fff" stroke-width="2.6"/></svg>understand what you have been told by your local physicians or specialist consultant</li>
      </ul>
    </section>

    <section class="offer offer--guidance">
      <h2>We'll give you guidance on...</h2>
      <ul>
        <li><svg width="14" height="12" viewBox="0 0 14 12"><path d="M1 6.5 5 10.5 13 1.5" fill="none" stroke="#fff" stroke-width="2.6"/></svg>whether the treatment or surgery your doctor suggests sounds appropriate</li>
        <li><svg width="14" height="12" viewBox="0 0 14 12"><path d="M1 6.5 5 10.5 13 1.5" fill="none" stroke="#fff" stroke-width="2.6"/></svg>whether it is up to date advice</li>
        <li><svg width="14" height="12" viewBox="0 0 14 12"><path d="M1 6.5 5 10.5 13 1.5" fill="none" stroke="#fff" stroke-width="2.6"/></svg>how to ask your local doctor clarifications or questions</li>
      </ul>
    </section>

    <section class="booking">
      <p class="booking-call">Book an appointment to discuss your case with us!</p>
      <p class="booking-link">http://www.theharborphysicians.example/book-an-appointment</p>
      <p class="booking-free">Get Basic Medical Health Info for FREE on Videos called Clinicasts</p>
    </section>

    <p class="brand-name">Harbor<br>Physicians</p>
  </main>
</body>
</html>
```